Medical Company in need of Modern business card design for new Wound Care clinic.

Modern business card design for our Woundcare company. Logo and description of services can be found on our website; https://www.tovrel-woundcare.com/

```html
<!DOCTYPE html>
<html lang="en">
<head>
<meta charset="utf-8">
<title>Tovrel Woundcare – Business Card</title>
<link href="https://fonts.googleapis.com/css2?family=Poppins:wght@400;600&family=Roboto:wght@400;500;700&display=swap" rel="stylesheet">
<style>
  :root {
    --backdrop: #2b2b2c;
    --card: #1f2022;
    --card-light: #2a2b2e;
    --gold: #c9973a;
    --gold-light: #e0b35a;
    --text-light: #e6e6e6;
    --text-dark: #1c1c1c;
  }
  * { margin: 0; padding: 0; box-sizing: border-box; }
  html, body { width: 1200px; height: 576px; overflow: hidden; background: var(--backdrop); }
  .stage { position: relative; width: 1200px; height: 576px; }
  .card {
    position: absolute; top: 138px; height: 294px; border-radius: 10px; overflow: hidden;
    background: radial-gradient(ellipse at 50% 20%, var(--card-light), var(--card) 70%);
  }
  .card--front { left: 102px; width: 484px; }
  .card--back { left: 596px; width: 481px; }

  .front-brand {
    position: absolute; left: 0; right: 0; top: 112px; text-align: center;
  }
  .front-brand__mark {
    display: block; width: 22px; height: 22px; margin: 0 auto 24px; background: var(--gold);
  }
  .front-brand__name {
    font-family: "Poppins", sans-serif; font-weight: 400; font-size: 30px;
    letter-spacing: 5px; color: var(--text-light);
  }

  .back-brand {
    position: absolute; left: 26px; top: 42px; display: flex; align-items: center; gap: 16px;
  }
  .back-brand__mark { width: 18px; height: 18px; background: var(--gold); }
  .back-brand__name {
    font-family: "Poppins", sans-serif; font-weight: 600; font-size: 28px;
    line-height: 27px; color: var(--text-light);
  }

  .person { position: absolute; left: 24px; top: 156px; font-family: "Roboto", sans-serif; }
  .person__name { font-size: 18px; font-weight: 700; color: var(--gold); }
  .person__title { font-size: 12.5px; color: var(--text-light); margin-top: 2px; }

  .address {
    position: absolute; left: 24px; top: 226px; font-family: "Roboto", sans-serif;
    font-size: 12.5px; line-height: 19px; color: var(--text-light);
  }

  .contacts {
    position: absolute; left: 258px; top: 162px; list-style: none;
    font-family: "Roboto", sans-serif; font-size: 12.5px; line-height: 19px; color: var(--text-light);
  }
  .contacts li { display: flex; align-items: center; gap: 6px; }
  .contacts svg { width: 10px; height: 10px; fill: var(--gold); }

  .service-band { position: absolute; left: 0; bottom: 0; width: 481px; height: 38px; }
  .service-band__text {
    position: absolute; right: 0; bottom: 12px; width: 270px; text-align: center;
    font-family: "Roboto", sans-serif; font-weight: 500; font-size: 12px; color: var(--text-dark);
  }
</style>
</head>
<body>
<div class="stage">
  <section class="card card--front">
    <div class="front-brand">
      <span class="front-brand__mark"></span>
      <div class="front-brand__name">TOVREL WOUNDCARE</div>
    </div>
  </section>

  <section class="card card--back">
    <div class="back-brand">
      <span class="back-brand__mark"></span>
      <div class="back-brand__name">TOVREL<br>WOUNDCARE</div>
    </div>

    <div class="person">
      <div class="person__name">Dr. Marin Tovrel</div>
      <div class="person__title">Managing Director</div>
    </div>

    <div class="address">2180 Larkspur Ave Ste 100<br>PMB 204517 Dallas, TX 75231</div>

    <ul class="contacts">
      <li><svg viewBox="0 0 10 10"><path d="M1 3 Q5 0 9 3 L8 4.5 L6.5 3.8 L6.5 3 Q5 2.5 3.5 3 L3.5 3.8 L2 4.5 Z M2.5 5 H7.5 L8.5 9 H1.5 Z"/></svg>972-555-0148</li>
      <li><svg viewBox="0 0 10 10"><path d="M0 2 H10 V8 H0 Z M0.6 2.5 L5 5.6 L9.4 2.5" stroke="#1f2022" stroke-width="0.8"/></svg>info@tovrel-woundcare.com</li>
      <li><svg viewBox="0 0 10 10"><circle cx="5" cy="5" r="4.5"/><path d="M0.5 5 H9.5 M5 0.5 V9.5 M5 0.5 Q2 5 5 9.5 M5 0.5 Q8 5 5 9.5" stroke="#1f2022" stroke-width="0.7" fill="none"/></svg>www.tovrel-woundcare.com</li>
    </ul>

    <svg class="service-band" viewBox="0 0 481 38" aria-hidden="true">
      <defs>
        <linearGradient id="goldFill" x1="0" x2="1">
          <stop offset="0" stop-color="#b8852e"/>
          <stop offset="0.5" stop-color="#e0b35a"/>
          <stop offset="1" stop-color="#c9973a"/>
        </linearGradient>
      </defs>
      <rect x="0" y="28" width="481" height="10" fill="url(#goldFill)"/>
      <path d="M212 0 H481 V38 H196 Z" fill="url(#goldFill)"/>
    </svg>
    <div class="service-band__text">All type of Wound Treatment &amp; HBO</div>
  </section>
</div>
</body>
</html>
```